Testing form re-design

I have 2 new testing forms in a very basic format, I need them updated to look similar to our other testing forms. Attached are the two new forms (Dermatology and GI) as well as a couple of our Original normal testing forms to compare them to. Needs to be in an editable PSD file incase I need to change the verbiage in the future. Also a few addendums to the Dermatology form - Need to add a form field for "Clinical Impression" as well as "Clinical History" with spaces 2 inches to handwrite next to them.

Industry/Entity Type

Healthcare

Font styles to use
Sans Serif

Colors

Designer to choose colors to be used in the design.

Requirements
Must have
• All the information on the current forms

```html
<!DOCTYPE html>
<html lang="en">
<head>
<meta charset="utf-8">
<title>Ridgeline Labs – Test Requisition Forms</title>
<link href="https://fonts.googleapis.com/css2?family=Poppins:ital,wght@0,400;0,500;0,600;0,700;1,400&display=swap" rel="stylesheet">
<style>
:root{
  --page:#c7daef;
  --band:#c5d9ee;
  --paper:#ffffff;
  --ink:#2b2b2b;
  --brand:#2a6db3;
  --navy:#34496b;
  --rule:#4a4a4a;
  --shade:#e4e4e4;
  --alert:#cf2e27;
}
*{box-sizing:border-box;margin:0;padding:0}
html,body{width:1200px;height:800px;overflow:hidden}
body{background:var(--page);font-family:'Poppins',sans-serif;color:var(--ink)}
.canvas{position:relative;width:1200px;height:800px;background:var(--page);overflow:hidden}
.sheet{position:absolute;top:39px;width:556px;height:724px;background:var(--paper);box-shadow:2px 2px 3px rgba(0,0,0,.22)}
.sheet--derm{left:29px}
.sheet--gi{left:614px}
.form{position:absolute;left:5px;top:4px;width:546px;height:716px;border-left:1px solid var(--rule);border-top:1px solid var(--rule)}
.cell{position:absolute;border-right:1px solid var(--rule);border-bottom:1px solid var(--rule);padding:3px 4px;font-size:6.2px;line-height:1.35}
.header{left:0;top:0;width:546px;height:70px;background:var(--band);padding:0}
.brand{position:absolute;left:8px;top:12px;display:flex;flex-direction:column;align-items:center}
.brand__dot{width:30px;height:30px;border-radius:50%;border:3px solid var(--navy)}
.brand__name{font-size:17px;font-weight:600;color:var(--brand);letter-spacing:.3px;margin-top:3px;line-height:1}
.title{position:absolute;left:180px;width:200px;top:17px;text-align:center;font-size:14px;font-weight:700;color:#333;line-height:1.3;letter-spacing:.2px}
.contact{position:absolute;right:4px;top:14px;text-align:right;font-size:7.6px;font-weight:600;color:#222;line-height:1.35}
.contact .web{margin-top:9px;font-size:8px}
.h{font-size:8.6px;font-weight:600;text-transform:uppercase;letter-spacing:.1px}
.b{font-weight:600}
.cb{display:inline-block;width:5.6px;height:5.6px;border:0.8px solid #333;vertical-align:-0.5px;margin-right:1.5px}
.sq{display:inline-block;width:5px;height:5px;background:#222;margin-right:3px;vertical-align:0}
.line{display:flex;align-items:flex-end;gap:2px;margin-top:2.2px}
.fill{flex:1;border-bottom:0.8px solid #333;height:6px}
.gap{width:6px}
.row{display:flex;justify-content:space-between}
.center{text-align:center}
.ul{text-decoration:underline;font-weight:600}
.cols{display:grid;gap:0 6px}
.tbl{display:grid;border-top:0.8px solid var(--rule);border-left:0.8px solid var(--rule)}
.tbl span{border-right:0.8px solid var(--rule);border-bottom:0.8px solid var(--rule);padding:1px 3px;font-size:6px;min-height:12px}
.shaded{background:var(--shade)}
.big{font-size:12px;font-weight:600;line-height:1}
.biopsy-body{padding:2px 3px;line-height:1.24}
.biopsy-body .line{margin-top:0}
.icd{position:absolute;border:1px solid var(--rule);font-size:7.6px;font-weight:500;padding:3px 4px}
.note{position:absolute;right:10px;font-size:6.6px;color:var(--alert);font-style:italic}
.legal{font-size:3.9px;line-height:1.4}
.legal .lt{font-size:4.6px;font-weight:700;margin:1px 0}
.legal ol{padding-left:10px}
.sig{display:flex;justify-content:flex-end;align-items:flex-end;gap:3px;font-size:4.8px;font-weight:700;margin:2px 0}
.sig .fill{flex:none;height:5px}
ul.dots{list-style:none}
ul.dots li::before{content:"•";margin-right:3px}
ul.dots li{font-size:6px;line-height:1.38;padding-left:3px}
.panel-head{font-size:6.5px;font-weight:600;font-style:italic;text-decoration:underline;margin-top:3px}
</style>
</head>
<body>
<div class="canvas">

<section class="sheet sheet--derm" aria-label="Dermatology test requisition form">
 <div class="form">
  <header class="cell header">
   <div class="brand"><span class="brand__dot"></span><span class="brand__name">RIDGELINE LABS</span></div>
   <h1 class="title">DERMATOLOGY<br>TEST REQUISITION FORM</h1>
   <div class="contact">4120 Lakeview Pkwy<br>Suite 210, Ferndale, MI 48220<div class="web">(248) 555-0147 | www.ridgelinelabs.com</div></div>
  </header>

  <div class="cell" style="left:0;top:70px;width:272px;height:135px"><div class="h">Ordering Physician/Laboratory</div></div>
  <div class="cell" style="left:0;top:205px;width:272px;height:24px;padding-top:5px;font-size:7px">Physician to receive additional result report:</div>
  <div class="cell" style="left:0;top:229px;width:137px;height:26px;font-size:7px">Clinical Impression:</div>
  <div class="cell" style="left:137px;top:229px;width:135px;height:26px;font-size:7px">Clinical History:</div>

  <div class="cell" style="left:272px;top:70px;width:274px;height:92px">
   <div class="row"><span class="h">Patient Information</span><span>Patient Demo Attached &nbsp;&nbsp;<span class="cb"></span></span></div>
   <div class="line">Last Name:<span class="fill"></span><span class="gap"></span>First Name:<span class="fill" style="flex:.7"></span></div>
   <div class="line">Middle Name:<span class="fill"></span><span class="gap"></span>Sex: <span class="cb"></span>Male <span class="cb"></span>Female<span style="width:30px"></span></div>
   <div class="line">Address:<span class="fill"></span></div>
   <div class="line">City:<span class="fill"></span><span class="gap"></span>State:<span class="fill" style="flex:.25"></span>Zip:<span class="fill" style="flex:.5"></span></div>
   <div class="line">DOB:<span class="fill"></span><span class="gap"></span>Mobile:<span class="fill"></span></div>
   <div class="line">Email:<span class="fill"></span></div>
  </div>
  <div class="cell" style="left:272px;top:162px;width:274px;height:33px">
   <div class="row"><span><span class="b" style="font-size:7px">Race:</span> <span class="cb"></span>Alaska Native or American Indian</span><span><span class="cb"></span>Asian</span><span><span class="cb"></span>Multiracial</span><span><span class="cb"></span>White</span></div>
   <div class="row"><span><span class="cb"></span>Black or African American</span><span><span class="cb"></span>Does not wish to disclose</span><span><span class="cb"></span>Not provided</span></div>
   <div><span class="cb"></span>Native Hawaiian or other Pacific Islander &nbsp;&nbsp;&nbsp;<span class="cb"></span>Other race</div>
  </div>
  <div class="cell" style="left:272px;top:195px;width:274px;height:34px">
   <div><span class="b" style="font-size:7px">Gender Identity:</span> <span class="cb"></span>Male <span class="cb"></span>Female <span class="cb"></span>Gender nonconforming <span class="cb"></span>Transgender</div>
   <div>male-to-female <span class="cb"></span>Transgender female-to-male &nbsp;<span class="cb"></span>Does not wish to disclose</div>
   <div><span class="cb"></span>Not provided <span class="cb"></span>Not applicable</div>
  </div>
  <div class="cell" style="left:272px;top:229px;width:274px;height:26px">
   <div><span class="b" style="font-size:7px">Sexual Orientation:</span><span class="cb"></span>Bisexual &nbsp;<span class="cb"></span>Straight &nbsp;<span class="cb"></span>Gay or Lesbian &nbsp;&nbsp;<span class="cb"></span>Others</div>
   <div><span class="cb"></span>Does not wish to disclose &nbsp;&nbsp;&nbsp;<span class="cb"></span>Not provided &nbsp;&nbsp;<span class="cb"></span>Not applicable</div>
  </div>

  <div class="cell" style="left:0;top:255px;width:546px;height:21px;padding-top:4px;white-space:nowrap">
   <span class="h">Billing Information</span> <span style="font-size:5.8px">(Please include a copy of the front &amp; back of card.)</span> <span class="b">Billing type:</span> <span class="cb"></span>Patient <span class="cb"></span>Insurance <span class="cb"></span>Client &nbsp;<span class="b">Relation:</span> <span class="cb"></span>Self <span class="cb"></span>Spouse <span class="cb"></span>Dependant
  </div>

  <div class="cell" style="left:0;top:276px;width:272px;height:228px;padding:0;overflow:hidden">
   <div style="padding:3px 4px;border-bottom:0.8px solid var(--rule);height:29px">
    <div class="h">Biopsy Information</div>
    <div class="b" style="font-size:7.4px">ICD 10 codes (required):</div>
   </div>
   <div style="display:grid;grid-template-columns:58px 62px 76px 1fr;border-bottom:0.8px solid var(--rule);height:18px">
    <span style="padding:1px 3px;border-right:0.8px solid var(--rule)">Date Collected</span>
    <span style="padding:1px 3px;border-right:0.8px solid var(--rule)">Time Collected</span>
    <span style="padding:1px 3px;border-right:0.8px solid var(--rule)">Collected Signature</span>
    <span style="padding:1px 3px">No of vials collected</span>
   </div>
   <div class="biopsy-body">
    <div><span class="b">Type:</span> D Punch Biopsy D &nbsp; D Shave Removal (Ink) &nbsp; D Shave Biopsy &nbsp; D Excision (Ink)</div>
    <div>D Alopecia Sections Punch Excision (Ink) &nbsp; D DIF &nbsp; D Currettage</div>
    <div class="cols" style="grid-template-columns:1fr 1fr;margin-top:3px;gap:3px 8px">
     <div><div class="line"><span class="big">1</span>Sites<span class="fill"></span></div><div class="b">Clinical Findings</div><div>D Nevus Atypical &nbsp; D SCC &nbsp; D FEP</div><div>D Melanoma DBCC &nbsp; D AK &nbsp; D DF</div><div>D SK &nbsp; DVV</div></div>
     <div><div class="line"><span class="big">3</span>Sites<span class="fill"></span></div><div class="b">Clinical Findings</div><div>D Nevus Atypical &nbsp; D SCC &nbsp; D FEP</div><div>D Melanoma DBCC &nbsp; D AK &nbsp; D DF</div><div>D SK &nbsp; DVV</div></div>
     <div><div class="line"><span class="big">2</span>Sites<span class="fill"></span></div><div class="b">Clinical Findings</div><div>D Nevus Atypical &nbsp; D SCC &nbsp; D FEP</div><div>D Melanoma DBCC &nbsp; D AK &nbsp; D DF</div><div>D SK &nbsp; DVV</div></div>
     <div><div class="line"><span class="big">4</span>Sites<span class="fill"></span></div><div class="b">Clinical Findings</div><div>D Nevus Atypical &nbsp; D SCC &nbsp; D FEP</div><div>D Melanoma DBCC &nbsp; D AK &nbsp; D DF</div><div>D SK &nbsp; DVV</div></div>
    </div>
    <div class="center ul" style="margin-top:4px;font-size:6.6px">ANTIMICROBIAL RESISTANCE PANEL</div>
    <div class="cols" style="grid-template-columns:1fr 1fr;padding-left:7px;margin-top:2px">
     <div>KPC-Carbapenem resistance<br>NDM-Carbapenem resistance<br>VIM-Carbapenem resistance<br>IMP-Carbapenem resistance<br>qnr-Quinolone resistance<br>vanB-Vancomycin resistance</div>
     <div>OXA-48-Carbapenem resistance<br>mecA/mecC-Methicilin resistance<br>CTX-M ESBL<br>sul-Sulfonamide resistance<br>vanA-Vancomycin resistance<br>dfrA-Trimethoprim resistance</div>
    </div>
   </div>
  </div>

  <div class="cell" style="left:272px;top:276px;width:274px;height:51px">
   <div class="line">Insured's SS#:<span class="fill"></span><span class="gap"></span>Insured's DOB:<span class="fill"></span></div>
   <div class="line">Primary Insurance Carrier:<span class="fill" style="flex:.5"></span>Medicare, Medicaid or Policy ID#:<span class="fill" style="flex:.5"></span></div>
   <div class="line">Claims Address:<span class="fill"></span></div>
   <div class="line">Employer/Group Name:<span class="fill"></span><span class="gap"></span>Group#:<span class="fill"></span></div>
  </div>
  <div class="cell" style="left:272px;top:327px;width:274px;height:18px">
   <div class="line" style="margin:0"><span class="h">Location of Infections:</span><span class="fill"></span></div>
  </div>
  <div class="cell" style="left:272px;top:345px;width:274px;height:159px;padding:0">
   <div class="shaded" style="height:15px;display:flex;align-items:center;justify-content:flex-end;gap:18px;padding-right:4px">
    <span style="font-size:9px;font-weight:600"><span class="cb" style="width:10px;height:7px"></span><span style="text-decoration:underline">Wound/Sepsis PCR Panel</span></span><span style="font-size:6.2px">Panel includes</span>
   </div>
   <div style="padding:2px 7px">
    <div class="center ul" style="font-size:6.6px">BACTERIA</div>
    <div class="cols" style="grid-template-columns:1fr 1fr">
     <div>Escherichia coli<br>Streptococcus agalactiae<br>Klebsiella oxytoca<br>Staphylococcus saprophyticus<br>Pseudomonas aeruginosa<br>Staphylococcus haemolyticus<br>Enterococcus faecium<br>Enterococcus faecalis</div>
     <div>Klebsiella aerogenes<br>Klebsiella pneumoniae<br>Staphylococcus aureus<br>Streptococcuspyogenes<br>Streptococcus pneumoniae<br>Streptococcus dysgalactiae<br>Staphylococcus lugdunensis<br>Staphylococcus epidermidis</div>
    </div>
    <div>Acinetobacter calcoaceticus-baumannii complex</div>
    <div class="center ul" style="font-size:6.6px;margin-top:2px">FUNGI</div>
    <div class="cols" style="grid-template-columns:1fr 1fr 1fr">
     <div>Candida krusei<br>Candida tropicalis<br>Candida glabrata</div>
     <div>Candida albicans<br>Fusarium solani<br>Microsporum spp</div>
     <div>Candida parapsilosis<br>Trychophyton spp</div>
    </div>
    <div class="center ul" style="font-size:6.6px;margin-top:2px">ANTIMICROBIAL RESISTANCE</div>
    <div class="center">Methicilin Resistance (MecA+C)</div>
   </div>
  </div>

  <div class="cell" style="left:0;top:504px;width:546px;height:76px">
   <div class="h">Other Test/Panels:</div>
   <div class="icd" style="left:392px;top:11px;width:130px;height:52px">ICD 10 codes (required):</div>
   <div class="note" style="top:65px">For a full menu of testing, please visit www.ridgelinelabs.com/menu</div>
  </div>

  <div class="cell legal" style="left:0;top:580px;width:546px;height:136px;padding:3px 6px">
   <div class="lt">Physician Authorization</div>
   <p>I, the undersigned healthcare provider, acknowledge that when ordering a panel through Ridgeline Labs, I understand and agree to the following terms:</p>
   <ol>
    <li>Specimens and related resistance marker tests may be forwarded to a partner reference laboratory for processing and analysis.</li>
    <li>Any pathology, cytology, and thin prep specimens will be forwarded to an affiliated pathology laboratory for evaluation and reporting.</li>
    <li>I understand that while the order is placed with Ridgeline Labs, testing may be performed by partner laboratories.</li>
    <li>I acknowledge that this referral process may affect billing procedures and timelines for results.</li>
    <li>I confirm that I have informed my patients about this testing arrangement as appropriate.</li>
   </ol>
   <div class="sig">Physician Signature <span class="fill" style="width:110px"></span> Date:<span class="fill" style="width:40px"></span></div>
   <div class="lt">Patient Consent and Authorization</div>
   <p>I authorize the release of my medical information, including test results, to my healthcare providers and insurance carriers. I request that payment of benefits be made to Ridgeline Labs on my behalf. I understand that I am liable for charges not covered by my insurer. I acknowledge the benefits, risks and limitations of this testing as described by a qualified healthcare provider. Medicare will only pay for services it determines to be reasonable and necessary. By signing below, I agree to assume financial responsibility for payment of these tests.</p>
   <div class="sig" style="margin-top:8px">Patient Signature <span class="fill" style="width:110px"></span> Date:<span class="fill" style="width:40px"></span></div>
  </div>
 </div>
</section>

<section class="sheet sheet--gi" aria-label="Gastrointestinal test requisition form">
 <div class="form">
  <header class="cell header">
   <div class="brand"><span class="brand__dot"></span><span class="brand__name">RIDGELINE LABS</span></div>
   <h1 class="title" style="left:176px;width:210px;top:16px">GASTROINTESTINAL (GI)<br>TEST REQUISITION FORM</h1>
   <div class="contact">4120 Lakeview Pkwy<br>Suite 210, Ferndale, MI 48220<div class="web">(248) 555-0147 | www.ridgelinelabs.com</div></div>
  </header>

  <div class="cell" style="left:0;top:70px;width:272px;height:135px"><div class="h">Ordering Physician/Laboratory</div></div>
  <div class="cell" style="left:0;top:205px;width:272px;height:24px;padding-top:5px;font-size:7px">Physician to receive additional result report:</div>
  <div class="cell" style="left:0;top:229px;width:137px;height:26px;font-size:7px">Clinical Impression:</div>
  <div class="cell" style="left:137px;top:229px;width:135px;height:26px;font-size:7px">Clinical History:</div>

  <div class="cell" style="left:272px;top:70px;width:274px;height:92px">
   <div class="row"><span class="h">Patient Information</span><span>Patient Demo Attached &nbsp;&nbsp;<span class="cb"></span></span></div>
   <div class="line">Last Name:<span class="fill"></span><span class="gap"></span>First Name:<span class="fill" style="flex:.7"></span></div>
   <div class="line">Middle Name:<span class="fill"></span><span class="gap"></span>Sex: <span class="cb"></span>Male <span class="cb"></span>Female<span style="width:30px"></span></div>
   <div class="line">Address:<span class="fill"></span></div>
   <div class="line">City:<span class="fill"></span><span class="gap"></span>State:<span class="fill" style="flex:.25"></span>Zip:<span class="fill" style="flex:.5"></span></div>
   <div class="line">DOB:<span class="fill"></span><span class="gap"></span>Mobile:<span class="fill"></span></div>
   <div class="line">Email:<span class="fill"></span></div>
  </div>
  <div class="cell" style="left:272px;top:162px;width:274px;height:33px">
   <div class="row"><span><span class="b" style="font-size:7px">Race:</span> <span class="cb"></span>Alaska Native or American Indian</span><span><span class="cb"></span>Asian</span><span><span class="cb"></span>Multiracial</span><span><span class="cb"></span>White</span></div>
   <div class="row"><span><span class="cb"></span>Black or African American</span><span><span class="cb"></span>Does not wish to disclose</span><span><span class="cb"></span>Not provided</span></div>
   <div><span class="cb"></span>Native Hawaiian or other Pacific Islander &nbsp;&nbsp;&nbsp;<span class="cb"></span>Other race</div>
  </div>
  <div class="cell" style="left:272px;top:195px;width:274px;height:34px">
   <div><span class="b" style="font-size:7px">Gender Identity:</span> <span class="cb"></span>Male <span class="cb"></span>Female <span class="cb"></span>Gender nonconforming <span class="cb"></span>Transgender</div>
   <div>male-to-female <span class="cb"></span>Transgender female-to-male &nbsp;<span class="cb"></span>Does not wish to disclose</div>
   <div><span class="cb"></span>Not provided <span class="cb"></span>Not applicable</div>
  </div>
  <div class="cell" style="left:272px;top:229px;width:274px;height:26px">
   <div><span class="b" style="font-size:7px">Sexual Orientation:</span><span class="cb"></span>Bisexual &nbsp;<span class="cb"></span>Straight &nbsp;<span class="cb"></span>Gay or Lesbian &nbsp;&nbsp;<span class="cb"></span>Others</div>
   <div><span class="cb"></span>Does not wish to disclose &nbsp;&nbsp;&nbsp;<span class="cb"></span>Not provided &nbsp;&nbsp;<span class="cb"></span>Not applicable</div>
  </div>

  <div class="cell" style="left:0;top:255px;width:546px;height:21px;padding-top:4px;white-space:nowrap">
   <span class="h">Billing Information</span> <span style="font-size:5.8px">(Please include a copy of the front &amp; back of card.)</span> <span class="b">Billing type:</span> <span class="cb"></span>Patient <span class="cb"></span>Insurance <span class="cb"></span>Client &nbsp;<span class="b">Relation:</span> <span class="cb"></span>Self <span class="cb"></span>Spouse <span class="cb"></span>Dependant
  </div>

  <div class="cell" style="left:0;top:276px;width:272px;height:233px;padding:0">
   <div style="padding:3px 4px;border-bottom:0.8px solid var(--rule);height:29px">
    <div class="h">Biopsy Information</div>
    <div class="b" style="font-size:7.4px">ICD 10 codes (required):</div>
   </div>
   <div style="display:grid;grid-template-columns:58px 62px 76px 1fr;border-bottom:0.8px solid var(--rule);height:18px">
    <span style="padding:1px 3px;border-right:0.8px solid var(--rule)">Date Collected</span>
    <span style="padding:1px 3px;border-right:0.8px solid var(--rule)">Time Collected</span>
    <span style="padding:1px 3px;border-right:0.8px solid var(--rule)">Collected Signature</span>
    <span style="padding:1px 3px">No of vials collected</span>
   </div>
   <div style="padding:1px 3px">
    <div class="b">Type:</div>
    <div><span class="cb"></span>Adenoma <span class="cb"></span>Crohn's <span class="cb"></span>H. pylori <span class="cb"></span>Microscopic Colitis <span class="cb"></span>Barrett's Esophagus</div>
    <div><span class="cb"></span>Dysplasia <span class="cb"></span>Hepatitis <span class="cb"></span>Proctitis <span class="cb"></span>Cancer <span class="cb"></span>Eosinophilic Esophagitis <span class="cb"></span>IBD</div>
    <div><span class="cb"></span>Sprue <span class="cb"></span>Candida <span class="cb"></span>Fungi <span class="cb"></span>Lymphoma <span class="cb"></span>Steatohepatitis <span class="cb"></span>Other:</div>
    <div class="b">Endoscopic Finding Code:</div>
    <div class="cols" style="grid-template-columns:62px 60px 52px 1fr;gap:0 2px;line-height:1.32">
     <div>1. Normal<br>2. Edema<br>3. Barrett's Mucosa<br>4. Granular<br>5. Nodular</div>
     <div>6. Friable<br>7. Erosion<br>8. Hyperemia<br>9. Telangiectactic<br>10. Polyp</div>
     <div>11. Hemorrahgic<br>12. Mass<br>13. Ulcer<br>14. Stricture<br>15. Polyposis</div>
     <div>16. Abn. Vascular Pattern<br>17. Punctate Hemorrhage<br>18. Submucosal Nodule<br>19. Pseudomembrane<br>20. Other:</div>
    </div>
    <div class="tbl" style="grid-template-columns:83px 45px 60px 1fr;margin-top:3px">
     <span class="b" style="line-height:1">Anatomic Site of Biopsy: Container</span><span class="b center">Organ &amp; Site</span><span class="b center">Distance (cm)</span><span class="b center" style="line-height:1">Endoscopic Finding (see codes above)</span>
     <span>1.</span><span></span><span></span><span></span>
     <span>2.</span><span></span><span></span><span></span>
     <span>3.</span><span></span><span></span><span></span>
     <span>4.</span><span></span><span></span><span></span>
     <span>5.</span><span></span><span></span><span></span>
    </div>
    <div style="margin-top:1px"><span class="b">Special stains for:</span> <span class="cb"></span>H. pylori <span class="cb"></span>Fungus <span class="cb"></span>TB <span class="cb"></span>Virus <span class="cb"></span>Other</div>
   </div>
  </div>

  <div class="cell" style="left:272px;top:276px;width:274px;height:51px">
   <div class="line">Insured's SS#:<span class="fill"></span><span class="gap"></span>Insured's DOB:<span class="fill"></span></div>
   <div class="line">Primary Insurance Carrier:<span class="fill" style="flex:.5"></span>Medicare, Medicaid or Policy ID#:<span class="fill" style="flex:.5"></span></div>
   <div class="line">Claims Address:<span class="fill"></span></div>
   <div class="line">Employer/Group Name:<span class="fill"></span><span class="gap"></span>Group#:<span class="fill"></span></div>
  </div>
  <div class="cell" style="left:272px;top:327px;width:274px;height:182px;padding:0">
   <div class="shaded center" style="height:14px;font-size:8.6px;font-weight:600;text-decoration:underline;line-height:14px">GI Panel</div>
   <div style="padding:1px 6px">
    <div class="panel-head"><span class="sq"></span>QX Prime Enteric Bacteria Panel <span class="cb"></span></div>
    <ul class="dots">
     <li>Salmonella spp &nbsp; • Campylobacter spp. (jejuni and coli)</li>
     <li>Shigella spp./Enteroinvasive E. coli (EIEC) &nbsp;• Yersinia enterocolitica</li>
     <li>Shiga toxin 1 &amp; 2 (E. coli [STEC], Shigella dysenteriae)</li>
     <li>Vibrio (V. vulvunificus, V. parahaemolyticus &amp; V. cholerae)</li>
     <li>Enterotoxigenic E. coli (ETEC) • Plesiomonas Shigelloides</li>
     <li>Specimen Types: Unpreserved soft to diarrheal stool, Cary-Blair preserved stool</li>
    </ul>
    <div class="panel-head"><span class="sq"></span>QX Prime Enteric Parasite Panel <span class="cb"></span></div>
    <ul class="dots">
     <li>Giardia Lamblia &nbsp;• Cryptosporidium (C. hominis and C. parvum)</li>
     <li>Entamoeba histolytica</li>
     <li>Specimen Types: Unpreserved soft to diarrheal stool, 10% Formalin fixed stool</li>
    </ul>
    <div class="panel-head"><span class="sq"></span>QX Prime Enteric Viral Panel <span class="cb"></span></div>
    <ul class="dots">
     <li>Norovirus GI/GII &nbsp;• Rotavirus A &nbsp;• Adenovirus F40/41</li>
     <li>Sapovirus (geno-groups I, II, IV, V) &nbsp;• Human Astrovirus (hAstro)</li>
     <li>Specimen Types: Unpreserved soft to diarrheal stool, Cary-Blair preserved stool</li>
    </ul>
    <div class="panel-head"><span class="sq"></span>QX Prime Cdiff Assay <span class="cb"></span></div>
    <ul class="dots">
     <li>Clostridium difficile toxin B gene (tcdB)</li>
     <li>Specimen Types: Unpreserved soft to diarrheal stool</li>
    </ul>
   </div>
  </div>

  <div class="cell" style="left:0;top:509px;width:546px;height:72px">
   <div class="h">Other Test/Panels:</div>
   <div class="icd" style="left:392px;top:6px;width:124px;height:52px">ICD 10 codes (required):</div>
   <div class="note" style="top:60px">For a full menu of testing, please visit www.ridgelinelabs.com/menu</div>
  </div>

  <div class="cell legal" style="left:0;top:581px;width:546px;height:135px;padding:3px 6px">
   <div class="lt">Physician Authorization</div>
   <p>I, the undersigned healthcare provider, acknowledge that when ordering a panel through Ridgeline Labs, I understand and agree to the following terms:</p>
   <ol>
    <li>Specimens and related resistance marker tests may be forwarded to a partner reference laboratory for processing and analysis.</li>
    <li>Any pathology, cytology, and thin prep specimens will be forwarded to an affiliated pathology laboratory for evaluation and reporting.</li>
    <li>I understand that while the order is placed with Ridgeline Labs, testing may be performed by partner laboratories.</li>
    <li>I acknowledge that this referral process may affect billing procedures and timelines for results.</li>
    <li>I confirm that I have informed my patients about this testing arrangement as appropriate.</li>
   </ol>
   <div class="sig">Physician Signature <span class="fill" style="width:110px"></span> Date:<span class="fill" style="width:40px"></span></div>
   <div class="lt">Patient Consent and Authorization</div>
   <p>I authorize the release of my medical information, including test results, to my healthcare providers and insurance carriers. I request that payment of benefits be made to Ridgeline Labs on my behalf. I understand that I am liable for charges not covered by my insurer. I acknowledge the benefits, risks and limitations of this testing as described by a qualified healthcare provider. Medicare will only pay for services it determines to be reasonable and necessary. By signing below, I agree to assume financial responsibility for payment of these tests.</p>
   <div class="sig" style="margin-top:8px">Patient Signature <span class="fill" style="width:110px"></span> Date:<span class="fill" style="width:40px"></span></div>
  </div>
 </div>
</section>

</div>
</body>
</html>
```